Powerpoint template for Trivia Company

Revamp of our current powerpoint template to make it more professional and fun for the players. Something worthy of a trivia company. Please see logo attached for potential colour - but also open to other ideas.

NO BRANDING REQUIRED (IE: No mention of our company or logo on the template please)

Target Market(s)

Bars/restaurants

Colors
3176b5
00a990

```html
<!DOCTYPE html>
<html lang="en">
<head>
<meta charset="utf-8">
<title>Trivia Night Presentation Template</title>
<link rel="stylesheet" href="https://fonts.googleapis.com/css2?family=Saira:wght@400;500;600;700&display=swap">
<style>
:root{
  --backdrop-top:#8ea9bf;
  --backdrop-bottom:#a6b89a;
  --slide-dark:#262626;
  --brand-blue:#0d5db4;
  --brand-blue-edge:#2f7fd6;
  --deep-blue:#073563;
  --deep-green:#2e5a14;
  --accent-green:#3f9a1e;
  --accent-green-edge:#6cc23c;
  --ink:#f2f2f2;
  --ink-soft:#cfcfcf;
  --tile:#1c1c1c;
  --tile-edge:#5a5a5a;
}
*{margin:0;padding:0;box-sizing:border-box}
html,body{width:1200px;height:739px;overflow:hidden}
body{
  font-family:"Saira",sans-serif;color:var(--ink);
  background:linear-gradient(160deg,var(--backdrop-top) 0%,#98acb0 50%,var(--backdrop-bottom) 100%);
  position:relative;
}
.slide{position:absolute;width:362px;height:203px;background:var(--slide-dark);overflow:hidden;box-shadow:0 2px 8px rgba(0,0,0,.25)}
.slide--brand{background:linear-gradient(200deg,var(--deep-blue) 0%,#164556 50%,var(--deep-green) 100%)}
.center{position:absolute;left:0;right:0;text-align:center}
.icon-tile{position:absolute;background:var(--tile);border:1px solid var(--tile-edge);border-radius:4px;display:flex;align-items:center;justify-content:center}
.icon-tile svg{stroke:var(--ink);fill:none;stroke-width:1.4;stroke-linecap:round;stroke-linejoin:round}
.pill{position:absolute;background:var(--brand-blue);border:1px solid var(--brand-blue-edge);border-radius:2px;display:flex;align-items:center;justify-content:center;text-align:center;font-size:8.6px;line-height:1.25;white-space:nowrap}
.welcome{top:100px;font-size:15px}
.title{top:119px;font-size:19px;font-weight:600}
.heading{font-size:12px;font-weight:400}
.rules-text{top:116px;font-size:11px;line-height:14.5px;white-space:nowrap}
.caption{font-size:8.5px;color:var(--ink-soft)}
.books{position:absolute;inset:0;background:linear-gradient(180deg,#6b5a47 0%,#4a4036 45%,#2b2a28 80%,#262626 100%)}
.progress{position:absolute;left:105px;top:178px;width:138px;height:4px;border:1px solid #777;border-radius:2px;background:#333}
.question{font-size:18.5px;line-height:24.5px;white-space:nowrap}
.numbers{position:absolute;left:98px;top:28px;width:165px;height:17px;border:1px solid #4b8a2a;border-radius:3px;display:flex;align-items:center;justify-content:space-around;font-size:8.5px;padding:0 2px}
.numbers .on{background:var(--accent-green);border:1px solid var(--accent-green-edge);border-radius:3px;width:15px;height:15px;display:flex;align-items:center;justify-content:center}
.answer{position:absolute;font-size:10.8px;display:flex;align-items:center;gap:9px;white-space:nowrap}
.badge{width:16px;height:16px;background:var(--accent-green);border:1px solid var(--accent-green-edge);border-radius:2px;display:flex;align-items:center;justify-content:center;font-size:8px}
.pass{top:111px;font-size:19px;line-height:25px}
.collab-q{top:83px;font-size:17px;line-height:22px;white-space:nowrap}
.winners{background:radial-gradient(ellipse 80px 160px at 50% 0%,#4a4a4a 0%,#2e2e2e 55%,#1c1c1c 100%)}
.podium-art{position:absolute;left:80px;top:95px;width:202px;height:90px;border-radius:4px;background:radial-gradient(ellipse at 50% 60%,#6a6a6a 0%,#3a3a3a 55%,rgba(28,28,28,0) 100%)}
</style>
</head>
<body>

<section class="slide slide--brand" style="left:41px;top:43px">
  <div class="icon-tile" style="left:161px;top:38px;width:39px;height:39px">
    <svg width="22" height="22" viewBox="0 0 24 24"><path d="M12 4v16M12 4c-2-2-6-1-6 2-3 1-3 5-1 6-2 2 0 6 3 5 1 3 4 3 4 0M12 4c2-2 6-1 6 2 3 1 3 5 1 6 2 2 0 6-3 5-1 3-4 3-4 0M8 9h2M14 12h3M8 15h2"/></svg>
  </div>
  <p class="center welcome">Welcome to</p>
  <h1 class="center title">THE TRIVIA NIGHT!</h1>
</section>

<section class="slide" style="left:421px;top:43px">
  <h2 class="center heading" style="top:16px">THE RULES</h2>
  <div class="icon-tile" style="left:31px;top:47px;width:39px;height:39px"><svg width="24" height="24" viewBox="0 0 24 24"><rect x="9" y="2" width="6" height="5"/><circle cx="8" cy="12" r="2.5"/><circle cx="16" cy="12" r="2.5"/><path d="M3 21c0-3 2-5 5-5s5 2 5 5M11 21c0-3 2-5 5-5s5 2 5 5"/></svg></div>
  <div class="icon-tile" style="left:75px;top:47px;width:39px;height:39px"><svg width="24" height="24" viewBox="0 0 24 24"><rect x="3" y="3" width="18" height="18" rx="3"/><path d="M9 13V7M12 12V6M15 12V7M9 13l-2-2M9 13v2c0 2 2 3 4 3s3-2 3-4V9"/></svg></div>
  <div class="icon-tile" style="left:119px;top:47px;width:39px;height:39px"><svg width="24" height="24" viewBox="0 0 24 24"><rect x="11" y="3" width="10" height="8" rx="1"/><rect x="3" y="10" width="10" height="8" rx="1"/><path d="M15 8l1-3 1 3M6 20l1-2M7 14h2"/></svg></div>
  <div class="icon-tile" style="left:163px;top:47px;width:39px;height:39px"><svg width="24" height="24" viewBox="0 0 24 24"><rect x="4" y="9" width="16" height="4"/><rect x="5" y="13" width="14" height="8"/><path d="M12 9v12M12 9c-2-4-6-4-5-1M12 9c2-4 6-4 5-1"/></svg></div>
  <div class="icon-tile" style="left:207px;top:47px;width:39px;height:39px"><svg width="24" height="24" viewBox="0 0 24 24"><path d="M12 3v17M7 21h10M4 6h16M6 6l-3 7h6zM18 6l-3 7h6z"/></svg></div>
  <div class="icon-tile" style="left:251px;top:47px;width:39px;height:39px"><svg width="24" height="24" viewBox="0 0 24 24"><circle cx="14" cy="6" r="2"/><path d="M13 9l-3 5 3 3-1 5M10 14l-3 7M13 9l4 4M11 10L7 5M5 3l4 4"/></svg></div>
  <div class="icon-tile" style="left:295px;top:47px;width:39px;height:39px"><svg width="24" height="24" viewBox="0 0 24 24"><circle cx="12" cy="5" r="2.5"/><path d="M5 21v-5c0-3 3-6 7-6s7 3 7 6v5M10 10l2 4 2-4M8 17l-2 2M16 17l2 2"/></svg></div>
  <p class="center rules-text">Before the game begins, each team must pick one<br>BONUS category (excluding the Final Trivia round)<br>for which they will be awarded double points.</p>
</section>

<section class="slide" style="left:801px;top:43px">
  <p class="center caption" style="top:15px">This quiz contains the following categories:</p>
  <div class="pill" style="left:23px;top:46px;width:155px;height:17px">General Knowledge</div>
  <div class="pill" style="left:23px;top:67px;width:155px;height:17px">One Word Movie Titles</div>
  <div class="pill" style="left:23px;top:88px;width:155px;height:31px">Name That Year – 2001-2010 Edition<br>(Each Year is Represented)</div>
  <div class="pill" style="left:23px;top:124px;width:155px;height:31px">Picture Round – One Letter Logos –<br>Name the Brand/Company</div>
  <div class="pill" style="left:189px;top:46px;width:155px;height:28px">Audio Round – Duets – Name the<br>Song and Both Artists</div>
  <div class="pill" style="left:189px;top:78px;width:155px;height:17px;font-size:8.2px">Hey Mom, I Got an “A” in Geography!</div>
  <div class="pill" style="left:189px;top:98px;width:155px;height:17px">Mmmmm.... Beer</div>
  <div class="pill" style="left:189px;top:118px;width:155px;height:17px">Final Trivia Round</div>
  <div class="pill" style="left:189px;top:139px;width:155px;height:17px">Tie Breaker Question</div>
</section>

<section class="slide" style="left:41px;top:264px">
  <div class="books" role="img" aria-label="Photo of a narrow aisle between towering shelves and stacks of old books"></div>
  <div class="pill" style="left:105px;top:148px;width:151px;height:23px;font-size:11.5px">General Knowledge</div>
  <div class="progress"></div>
  <svg style="position:absolute;left:247px;top:176px" width="9" height="9" viewBox="0 0 10 10"><path d="M1 0v10" stroke="#eee"/><path d="M1 1h8v5H1z" fill="#eee"/><path d="M1 1h2v2.5H1zM5 1h2v2.5H5zM3 3.5h2V6H3zM7 3.5h2V6H7z" fill="#222"/></svg>
</section>

<section class="slide" style="left:421px;top:264px">
  <p class="center caption" style="top:10px">General Knowledge</p>
  <div class="numbers"><span>1</span><span class="on">2</span><span>3</span><span>4</span><span>5</span><span>6</span><span>7</span><span>8</span><span>9</span><span>10</span></div>
  <p class="center question" style="top:62px">In the language of<br>international warfare, what<br>do the letters SAM mean?</p>
</section>

<section class="slide" style="left:801px;top:264px">
  <h2 class="center heading" style="top:17px;font-size:12.5px">ANSWERS</h2>
  <div class="answer" style="left:41px;top:57px"><span class="badge">1</span>Tuxedo</div>
  <div class="answer" style="left:41px;top:79px"><span class="badge">2</span>Surface to Air Missile</div>
  <div class="answer" style="left:41px;top:102px"><span class="badge">3</span>Kendra (born in 1979)</div>
  <div class="answer" style="left:41px;top:124px"><span class="badge">4</span>Thomas Whitfield</div>
  <div class="answer" style="left:41px;top:146px"><span class="badge">5</span>Tracey Oldham</div>
  <div class="answer" style="left:196px;top:57px"><span class="badge">6</span>When Nature Calls</div>
  <div class="answer" style="left:196px;top:79px"><span class="badge">7</span>Nadira Bashir</div>
  <div class="answer" style="left:196px;top:102px"><span class="badge">8</span>The Harbor City Larks</div>
  <div class="answer" style="left:196px;top:124px"><span class="badge">9</span>Mercury</div>
  <div class="answer" style="left:196px;top:146px"><span class="badge">10</span>Iceland</div>
</section>

<section class="slide" style="left:41px;top:486px">
  <div class="icon-tile" style="left:161px;top:47px;width:39px;height:39px">
    <svg width="22" height="22" viewBox="0 0 24 24"><path d="M4 8h15M15 4l4 4-4 4M20 16H5M9 12l-4 4 4 4"/></svg>
  </div>
  <p class="center pass">Please Pass your answers<br>to a neighboring team.</p>
</section>

<section class="slide slide--brand" style="left:421px;top:486px">
  <div class="icon-tile" style="left:168px;top:19px;width:26px;height:26px">
    <svg width="13" height="13" viewBox="0 0 10 10" style="stroke:none"><path d="M1 0v10" stroke="#eee"/><path d="M1 1h8v5H1z" fill="#eee"/><path d="M1 1h2v2.5H1zM5 1h2v2.5H5zM3 3.5h2V6H3zM7 3.5h2V6H7z" fill="#222"/></svg>
  </div>
  <p class="center caption" style="top:54px">Movie Star Collaborations</p>
  <p class="center collab-q">Name 3 of the 4 films that<br>Jenna Lawson and Brady<br>Cole have starred in together.</p>
</section>

<section class="slide winners" style="left:801px;top:486px">
  <p class="center" style="top:45px;font-size:17.5px">Congratulations to the winners!</p>
  <div class="podium-art" role="img" aria-label="Illustration of a spotlit winners podium with places 1, 2 and 3"></div>
</section>

</body>
</html>
```